Sticker Design Project

I want a design for my new synthetic 10W/50 motor oil.
It will be of international standard since it will be offered in several countries.
We are a lubricant manufacturing and marketing company operating in several African countries.

Target Market(s)

Top range car owners and garages

Industry/Entity Type

Marketing

Requirements
Must have
• images related to autos

```html
<!DOCTYPE html>
<html lang="en">
<head>
<meta charset="UTF-8">
<title>Ironclad Apex – Synthetic Motor Oil Label</title>
<link href="https://fonts.googleapis.com/css2?family=Oswald:wght@500;700&display=swap" rel="stylesheet">
<style>
  :root {
    --page-bg: #d6d6d6;
    --label-black: #121212;
    --carbon: #1d1d1f;
    --red-deep: #9e0a0e;
    --red-bright: #e0141b;
    --blue-deep: #1f2357;
    --blue-mid: #3b3f8c;
    --gold-light: #e6c15a;
    --gold-dark: #7a5a18;
    --chrome-light: #d9dadd;
    --chrome-dark: #5b5d63;
    --orange: #f39a1e;
    --white: #ffffff;
    --badge-purple: #4b1640;
  }
  html, body {
    margin: 0;
    padding: 0;
    width: 1200px;
    height: 1200px;
    overflow: hidden;
    background: var(--page-bg);
  }
  .label {
    position: absolute;
    left: 210px;
    top: 75px;
    width: 780px;
    height: 1050px;
    border-radius: 22px;
    overflow: hidden;
    background: var(--label-black);
    font-family: 'Oswald', sans-serif;
  }
  .label__art {
    position: absolute;
    inset: 0;
    width: 780px;
    height: 1050px;
  }
  .product-name {
    position: absolute;
    right: 90px;
    top: 300px;
    margin: 0;
    text-align: right;
    color: var(--white);
    font-weight: 700;
    font-size: 108px;
    line-height: 1.02;
    letter-spacing: 1px;
  }
  .product-name__mark {
    position: absolute;
    right: 40px;
    top: 315px;
    width: 44px;
    height: 44px;
    border-radius: 50%;
    background: var(--orange);
  }
  .product-subtitle {
    position: absolute;
    right: 90px;
    top: 540px;
    margin: 0;
    color: var(--white);
    font-weight: 500;
    font-size: 29px;
    letter-spacing: 0.3px;
  }
  .grade-badge {
    position: absolute;
    right: 0;
    top: 905px;
    width: 320px;
    height: 92px;
    border-radius: 20px 0 0 20px;
    background: linear-gradient(90deg, var(--red-bright) 0%, var(--red-deep) 55%, var(--badge-purple) 100%);
    display: flex;
    align-items: center;
    justify-content: center;
  }
  .grade-badge__text {
    color: var(--white);
    font-weight: 700;
    font-size: 62px;
    letter-spacing: 1px;
  }
</style>
</head>
<body>
  <div class="label">
    <svg class="label__art" viewBox="0 0 780 1050" xmlns="http://www.w3.org/2000/svg">
      <defs>
        <linearGradient id="redTop" x1="0" y1="0" x2="1" y2="1">
          <stop offset="0" stop-color="var(--red-deep)"/>
          <stop offset="0.5" stop-color="var(--red-bright)"/>
          <stop offset="1" stop-color="var(--red-deep)"/>
        </linearGradient>
        <radialGradient id="carbonGlow" cx="0.5" cy="0.45" r="0.6">
          <stop offset="0" stop-color="#2a2a2c"/>
          <stop offset="1" stop-color="var(--label-black)"/>
        </radialGradient>
        <linearGradient id="chrome" x1="0" y1="0" x2="1" y2="1">
          <stop offset="0" stop-color="var(--chrome-light)"/>
          <stop offset="0.6" stop-color="var(--chrome-dark)"/>
          <stop offset="1" stop-color="#2b2b2e"/>
        </linearGradient>
        <linearGradient id="gold" x1="0" y1="0" x2="1" y2="1">
          <stop offset="0" stop-color="var(--gold-light)"/>
          <stop offset="1" stop-color="var(--gold-dark)"/>
        </linearGradient>
        <linearGradient id="gears" x1="0" y1="0" x2="1" y2="1">
          <stop offset="0" stop-color="var(--blue-mid)"/>
          <stop offset="1" stop-color="var(--blue-deep)"/>
        </linearGradient>
      </defs>

      <rect class="carbon-field" width="780" height="1050" fill="url(#carbonGlow)"/>

      <path class="top-band" d="M0 0 H780 V340 C640 190 380 140 0 200 Z" fill="url(#redTop)"/>

      <path class="gears-field" role="img" aria-label="Photo of dark blue engine gears"
            d="M0 930 C260 880 560 760 780 560 V1050 H0 Z" fill="url(#gears)"/>

      <path class="red-swoosh" d="M0 905 C260 860 560 740 780 535 V565 C560 770 260 895 0 935 Z" fill="var(--red-bright)"/>

      <rect class="rider-photo" role="img" aria-label="Photo of a rider on a silver sport motorcycle with flames trailing behind"
            x="290" y="25" width="380" height="260" rx="30" fill="url(#chrome)" opacity="0.85"/>

      <rect class="pistons-photo" role="img" aria-label="Photo of golden engine pistons and crankshaft"
            x="0" y="560" width="390" height="340" rx="30" fill="url(#gold)" opacity="0.9"/>
    </svg>

    <h1 class="product-name">IRONCLAD<br>APEX</h1>
    <span class="product-name__mark"></span>
    <p class="product-subtitle">New Synthetic Motor OIL</p>

    <div class="grade-badge"><span class="grade-badge__text">10W/50</span></div>
  </div>
</body>
</html>
```